Bref créative
TRV Construction Supplies Stationary Package
Complete Stationary Package, Biz Cards, Letterhead, Folder, Comp Slips
Professional
Owen Pellig
Marketing Executive
Unit K
Ridgefield Distribution Centre
Harcombe Way
Avonmouth
Bristol
BS10 4QJ
owenpellig@tumblingkite.co.uk
www.trvcs.co.uk
Would like options using either of the backgrounds we have provided.....
Would like the back of our business card to use the black background logo.

```html
<!DOCTYPE html>
<html lang="en">
<head>
<meta charset="utf-8">
<title>TRV Construction Supplies — Stationery Package</title>
<link rel="stylesheet" href="https://fonts.googleapis.com/css2?family=Montserrat:wght@400;600;700&family=Great+Vibes&display=swap">
<style>
  :root {
    --stage: #3a2c25;
    --paper: #ffffff;
    --ink: #333333;
    --muted: #777777;
    --orange: #f39a1e;
    --orange-deep: #e4700b;
    --orange-light: #fbbf3f;
    --grey: #b9b9b9;
    --grey-dark: #8c8c8c;
    --black: #1b1b1b;
  }
  * { box-sizing: border-box; margin: 0; padding: 0; }
  html, body { width: 1200px; height: 852px; overflow: hidden; }
  body { background: var(--stage); font-family: "Montserrat", Arial, sans-serif; color: var(--ink); position: relative; }

  .piece { position: absolute; background: var(--paper); overflow: hidden; box-shadow: 0 3px 8px rgba(0,0,0,.35); }
  .piece svg.swoosh { position: absolute; left: 0; bottom: 0; width: 100%; }

  .brand { position: absolute; text-align: center; line-height: 1; }
  .brand__name { font-weight: 700; color: var(--orange-deep); letter-spacing: .04em; text-transform: uppercase; white-space: nowrap; }
  .brand__mark { display: inline-block; background: var(--orange); vertical-align: middle; margin-right: .35em; }
  .brand__tag { font-weight: 400; color: var(--muted); letter-spacing: .08em; text-transform: uppercase; margin-top: 3px; white-space: nowrap; }

  .small-text { font-size: 4px; line-height: 1.5; color: var(--ink); white-space: pre; position: absolute; }

  /* business cards */
  .card { width: 137px; height: 56px; top: 113px; }
  .card--front-a { left: 43px; }
  .card--front-b { left: 192px; }
  .card--back { left: 115px; top: 235px; height: 60px; background: var(--black); }
  .card--back .small-text { color: #dddddd; }

  /* envelopes & slips */
  .envelope-c5 { left: 36px; top: 353px; width: 307px; height: 197px; }
  .comp-slip { left: 96px; top: 509px; width: 276px; height: 115px; }
  .envelope-dl { left: 406px; top: 593px; width: 293px; height: 122px; }
  .script { font-family: "Great Vibes", cursive; color: var(--grey-dark); position: absolute; }

  /* letterhead */
  .letterhead { left: 377px; top: 101px; width: 326px; height: 432px; }

  /* folder */
  .folder-cover { left: 742px; top: 221px; width: 220px; height: 280px; }
  .folder-inner-right { left: 962px; top: 221px; width: 224px; height: 280px; box-shadow: 2px 3px 8px rgba(0,0,0,.35); }
  .folder-inside { left: 742px; top: 509px; width: 444px; height: 276px; }
  .folder-cover__band { position: absolute; left: 0; top: 0; width: 100%; height: 48px; background: var(--black); }
</style>
</head>
<body>

<svg width="0" height="0" style="position:absolute" aria-hidden="true">
  <defs>
    <linearGradient id="orangeFill" x1="0" y1="0" x2="1" y2="1">
      <stop offset="0" stop-color="#fbbf3f"/>
      <stop offset=".55" stop-color="#f39a1e"/>
      <stop offset="1" stop-color="#e4700b"/>
    </linearGradient>
    <linearGradient id="greyFill" x1="0" y1="0" x2="1" y2="0">
      <stop offset="0" stop-color="#e6e6e6"/>
      <stop offset="1" stop-color="#9a9a9a"/>
    </linearGradient>
  </defs>
</svg>

<!-- Business card front A -->
<div class="piece card card--front-a">
  <div class="brand" style="left:0;right:0;top:10px;">
    <div class="brand__name" style="font-size:6px;"><span class="brand__mark" style="width:5px;height:5px;"></span>TRV Construction Supplies</div>
    <div class="brand__tag" style="font-size:3px;">Supplying every build project</div>
  </div>
  <div class="small-text" style="left:8px;top:32px;">Owen Pellig
Marketing Executive</div>
  <svg class="swoosh" viewBox="0 0 137 20" preserveAspectRatio="none" height="20">
    <path d="M0 18 Q70 14 137 0 L137 20 L0 20Z" fill="url(#greyFill)"/>
    <path d="M40 20 Q100 14 137 4 L137 20Z" fill="url(#orangeFill)"/>
  </svg>
</div>

<!-- Business card front B -->
<div class="piece card card--front-b">
  <div class="brand" style="left:0;right:0;top:10px;">
    <div class="brand__name" style="font-size:6px;"><span class="brand__mark" style="width:5px;height:5px;"></span>TRV Construction Supplies</div>
    <div class="brand__tag" style="font-size:3px;">Supplying every build project</div>
  </div>
  <div class="small-text" style="left:8px;top:32px;">Owen Pellig
Marketing Executive</div>
  <svg class="swoosh" viewBox="0 0 137 20" preserveAspectRatio="none" height="20">
    <path d="M0 20 Q60 8 137 2 L137 20Z" fill="url(#orangeFill)"/>
    <path d="M0 20 Q60 12 137 9 L137 20Z" fill="url(#greyFill)"/>
  </svg>
</div>

<!-- Business card back -->
<div class="piece card card--back">
  <div class="brand" style="left:8px;top:12px;text-align:left;">
    <div class="brand__name" style="font-size:5px;color:var(--orange);"><span class="brand__mark" style="width:4px;height:4px;"></span>TRV Construction Supplies</div>
  </div>
  <div class="small-text" style="left:62px;top:24px;">Unit K, Ridgefield Distribution Centre
Harcombe Way, Avonmouth, Bristol BS10 4QJ
T: 0117 496 0382
owenpellig@tumblingkite.co.uk
www.trvcs.co.uk</div>
</div>

<!-- C5 envelope -->
<div class="piece envelope-c5">
  <svg viewBox="0 0 307 100" preserveAspectRatio="none" width="307" height="100" style="position:absolute;left:0;top:0;">
    <path d="M0 0 L307 0 L307 34 Q153 82 0 34Z" fill="url(#orangeFill)"/>
    <path d="M0 34 Q153 82 307 34 L307 44 Q153 96 0 44Z" fill="url(#greyFill)"/>
  </svg>
  <div class="brand" style="left:0;right:0;top:14px;">
    <div class="brand__name" style="font-size:8px;color:var(--paper);"><span class="brand__mark" style="width:6px;height:6px;background:var(--paper);"></span>TRV Construction Supplies</div>
  </div>
</div>

<!-- Comp slip -->
<div class="piece comp-slip">
  <div class="brand" style="left:10px;top:14px;text-align:left;">
    <div class="brand__name" style="font-size:7px;"><span class="brand__mark" style="width:6px;height:6px;"></span>TRV Construction Supplies</div>
    <div class="brand__tag" style="font-size:3.5px;">Supplying every build project</div>
  </div>
  <div class="small-text" style="left:10px;top:44px;">Unit K, Ridgefield Distribution Centre
Harcombe Way, Avonmouth, Bristol BS10 4QJ</div>
  <svg class="swoosh" viewBox="0 0 276 34" preserveAspectRatio="none" height="34">
    <path d="M0 8 Q140 30 276 0 L276 34 L0 34Z" fill="url(#orangeFill)"/>
    <path d="M0 16 Q140 36 276 12 L276 34 L0 34Z" fill="url(#greyFill)"/>
  </svg>
</div>

<!-- Letterhead -->
<div class="piece letterhead">
  <div class="brand" style="left:22px;top:26px;text-align:left;">
    <div class="brand__name" style="font-size:8px;"><span class="brand__mark" style="width:7px;height:7px;"></span>TRV Construction Supplies</div>
    <div class="brand__tag" style="font-size:4px;">Supplying every build project</div>
  </div>
  <div class="small-text" style="left:226px;top:24px;">Unit K
Ridgefield Distribution Centre
Harcombe Way
Avonmouth, Bristol BS10 4QJ</div>
  <div class="small-text" style="left:22px;top:330px;">T: 0117 496 0382
F: 0117 496 0383
www.trvcs.co.uk</div>
  <svg class="swoosh" viewBox="0 0 326 70" preserveAspectRatio="none" height="70">
    <path d="M0 40 Q180 60 326 10 L326 70 L0 70Z" fill="url(#greyFill)"/>
    <path d="M0 50 Q180 66 326 22 L326 70 L0 70Z" fill="url(#orangeFill)"/>
  </svg>
</div>

<!-- DL envelope -->
<div class="piece envelope-dl">
  <div class="brand" style="left:14px;top:16px;text-align:left;">
    <div class="brand__name" style="font-size:7px;"><span class="brand__mark" style="width:6px;height:6px;"></span>TRV Construction Supplies</div>
    <div class="brand__tag" style="font-size:3.5px;">Supplying every build project</div>
  </div>
  <svg class="swoosh" viewBox="0 0 293 40" preserveAspectRatio="none" height="40">
    <path d="M0 10 Q150 36 293 8 L293 40 L0 40Z" fill="url(#greyFill)"/>
    <path d="M0 22 Q150 40 293 18 L293 40 L0 40Z" fill="url(#orangeFill)"/>
  </svg>
  <div class="script" style="right:14px;bottom:8px;font-size:11px;color:#5b3d16;">With Compliments</div>
</div>

<!-- Folder cover -->
<div class="piece folder-cover">
  <div class="folder-cover__band"></div>
  <div class="brand" style="left:0;right:0;top:64px;">
    <div class="brand__name" style="font-size:9px;"><span class="brand__mark" style="width:8px;height:8px;"></span>TRV Construction Supplies</div>
    <div class="brand__tag" style="font-size:4px;">Supplying every build project</div>
  </div>
  <svg class="swoosh" viewBox="0 0 220 170" preserveAspectRatio="none" height="170">
    <path d="M0 20 Q110 0 220 40 L220 170 L0 170Z" fill="url(#orangeFill)"/>
  </svg>
</div>

<!-- Folder inner right with pocket -->
<div class="piece folder-inner-right">
  <svg viewBox="0 0 224 280" preserveAspectRatio="none" width="224" height="280" style="position:absolute;left:0;top:0;">
    <path d="M0 0 L224 0 L224 140 L0 140Z" fill="url(#orangeFill)"/>
    <path d="M0 70 Q120 20 224 30 L224 280 L0 280Z" fill="var(--paper)"/>
    <path d="M0 250 Q120 240 224 200 L224 280 L0 280Z" fill="url(#orangeFill)"/>
    <path d="M0 250 Q120 240 224 200 L224 206 Q120 246 0 256Z" fill="url(#greyFill)"/>
  </svg>
  <div class="brand" style="left:0;right:0;top:110px;">
    <div class="brand__name" style="font-size:7px;"><span class="brand__mark" style="width:6px;height:6px;"></span>TRV Construction Supplies</div>
    <div class="brand__tag" style="font-size:3.5px;">Supplying every build project</div>
  </div>
  <div class="small-text" style="left:78px;top:140px;">Unit K
Ridgefield Distribution Centre
Harcombe Way
Avonmouth
Bristol
BS10 4QJ
www.trvcs.co.uk</div>
</div>

<!-- Folder inside spread -->
<div class="piece folder-inside">
  <svg viewBox="0 0 444 276" preserveAspectRatio="none" width="444" height="276" style="position:absolute;left:0;top:0;">
    <path d="M0 150 Q0 100 60 100 Q170 100 210 276 L0 276Z" fill="url(#orangeFill)"/>
    <path d="M444 150 Q444 100 384 100 Q274 100 234 276 L444 276Z" fill="url(#orangeFill)"/>
    <path d="M210 276 Q222 240 234 276Z" fill="#dddddd"/>
  </svg>
</div>

</body>
</html>
```